Company's Core Values to be on our Office Walls

We are a biotechnology consulting company in Massachusetts with about 40 employees. Please check out quelvo.com for our look and more information on our business.

We have 4 core values in the company which we would like to display in our office. (Could be on our walls, could be placed in our website, could be placed anywhere. - We would like a multi-use for this graphic but PRIMARILY on our walls.)
No measurements involved yet, hence we'd like the source file to enable us to stretch the graphics. What's important is to see the designs in this contest.

Design: Looking for a wall display - decal, glass board, vinyl (we're open)
- of our Core Values to have in our reception. We want a Double-Helix
incorporated as the core values are "in our DNA" like the one attached
(would like to see some designs with the exact photo and some used as
inspiration for a unique creative design). Open to various sizes, we have a
few different walls we could place them on.

We are looking for a creative Core Value display to have in our new office. We want a sleek, out of the box design!

Quelvo's 4 Core Values are:
> Put Others First
> Have the Courage to Take Action
> Take Personal Responsibility
> Have fun!
***We welcome any infographics per core value. We are open to your creativity!

**WE WANT THE ACTUAL CORE VALUES ON DISPLAY**
We already have a brand (attached).
Need our actual values on display in office.
We want the actual values on the wall, our logo can be incorporated but not
necessarily.

Overview of company: Young consulting firm for biotech and pharmaceuticals
in the Greater Boston area. We are service based, our employees are
engineers and specialists that work on our clients site. Company was
established in 2010, we moved into our New England office 3 months ago!

Colors: Our main color is blue but we also use orange, green, purple, and
teal. See quelvo.com for our colors.

Target Market(s)

New Hires and Clients - We want to impress them!
Employees and clients - we want employees inspired by the core
values and clients to be impressed by them/separate us from the competition.

Industry/Entity Type

Biotechnology

Font styles to use
Sans Serif

Colors

Designer to choose colors to be used in the design.

Requirements
Must have
• Creativity!
• Some sort of tie to science/biotech
• Color - Blue is our company color but would like others as well. See website for brand colors.

```html
<!DOCTYPE html>
<html lang="en">
<head>
<meta charset="utf-8">
<title>Core Values Wall Display</title>
<link rel="stylesheet" href="https://fonts.googleapis.com/css2?family=Exo+2:wght@800&display=swap">
<style>
  :root {
    --navy: #0e3a5c;
    --paper: #ffffff;
    --pattern: #ececec;
  }
  html, body {
    margin: 0;
    padding: 0;
    width: 1200px;
    height: 1200px;
    overflow: hidden;
    background: var(--paper);
  }
  .values-board {
    display: block;
    width: 1200px;
    height: 1200px;
  }
  .value-label {
    font-family: "Exo 2", sans-serif;
    font-weight: 800;
    fill: var(--navy);
  }
  .brand-name {
    font-family: "Exo 2", sans-serif;
    font-weight: 800;
    fill: var(--paper);
    font-size: 19px;
  }
  .link {
    stroke: var(--navy);
    stroke-width: 1.8;
    fill: none;
  }
  .node {
    fill: var(--paper);
    stroke: var(--navy);
    stroke-width: 1.8;
  }
  .brand-disc {
    fill: var(--navy);
  }
</style>
</head>
<body>
<svg class="values-board" viewBox="0 0 1200 1200" xmlns="http://www.w3.org/2000/svg">
  <defs>
    <radialGradient id="moleculeTone" cx="0.7" cy="0.4" r="0.6">
      <stop offset="0" stop-color="#f1f1f1"/>
      <stop offset="1" stop-color="#ffffff"/>
    </radialGradient>
  </defs>

  <rect class="molecule-field" x="300" y="0" width="900" height="1200" fill="url(#moleculeTone)" role="img" aria-label="Faint grey molecular network pattern of linked circles"/>

  <g class="values-graphic" transform="translate(-280.8 170.4) scale(1.2)">
    <g class="connectors">
      <line class="link" x1="677" y1="330" x2="680" y2="468"/>
      <line class="link" x1="712" y1="283" x2="740" y2="271"/>
      <line class="link" x1="753" y1="295" x2="758" y2="285"/>
      <line class="link" x1="758" y1="308" x2="835" y2="372"/>
      <line class="link" x1="792" y1="370" x2="833" y2="375"/>
      <line class="link" x1="840" y1="382" x2="836" y2="421"/>
      <line class="link" x1="744" y1="436" x2="745" y2="416"/>
      <line class="link" x1="754" y1="449" x2="800" y2="450"/>
      <line class="link" x1="732" y1="455" x2="705" y2="474"/>

      <path class="link" d="M 765 225 A 30 30 0 1 0 790 272"/>
      <path class="link" d="M 696 270 A 32 32 0 0 1 688 332"/>
      <path class="link" d="M 846 427 A 30 30 0 0 0 840 482"/>
      <path class="link" d="M 680 468 A 32 32 0 0 1 675 532"/>
    </g>

    <g class="nodes">
      <circle class="node" cx="753" cy="302" r="7"/>
      <circle class="node" cx="840" cy="375" r="7"/>
      <circle class="node" cx="742" cy="448" r="12"/>
    </g>

    <g class="brand-mark">
      <circle class="brand-disc" cx="746" cy="368" r="48"/>
      <text class="brand-name" x="746" y="375" text-anchor="middle">Verant</text>
    </g>

    <g class="value-put-others">
      <text class="value-label" x="766" y="217" font-size="34">PUT OTHERS</text>
      <text class="value-label" x="766" y="259" font-size="34">FIRST</text>
    </g>

    <g class="value-courage">
      <text class="value-label" x="695" y="268" font-size="29.5" text-anchor="end">HAVE THE COURAGE</text>
      <text class="value-label" x="695" y="306" font-size="29.5" text-anchor="end">TO TAKE ACTION</text>
    </g>

    <g class="value-responsibility">
      <text class="value-label" x="818" y="467" font-size="30.5">TAKE PERSONAL</text>
      <text class="value-label" x="818" y="505" font-size="30.5">RESPONSIBILITY</text>
    </g>

    <g class="value-fun">
      <text class="value-label" x="692" y="520" font-size="29.5" text-anchor="end">HAVE FUN!</text>
    </g>
  </g>
</svg>
</body>
</html>
```